Homepage of voice message app

We are developing a mobile application of which one of the more important features is a voice to transcript.

What we would like to have designed is a basic interface that would show one ore more avatars on a home screen + the following functionalities:
- record
-while recording there should be three functions included in buttons (delete last sentence / send / send & next message (i.e. keep the recording going))
&
- listen (to new message)
- while listening replies should be possible in the form of emoticons (only emoticons, no text)

Attached:
-an example of the style we appreciate

Target Market(s)

English speaking Millenials

Industry/Entity Type

Messaging

Font styles to use
Sans Serif

Requirements
Must have
• My project must have a clean design and should not be too futuristic. We are targetting an average person between 20-80 years.
Nice to have
• We would like to focus on a minimum amount of finger movements to get the message across, we prefer simple tabs and swipes within the home screen to access the features.
Should not have
• The project should not have too many moving pieces within the screen.

```html
<!DOCTYPE html>
<html lang="en">
<head>
<meta charset="utf-8">
<title>Homepage – Voice Message App</title>
<link href="https://fonts.googleapis.com/css2?family=Montserrat:wght@700;800&family=Poppins:wght@300;400;500;600;700&display=swap" rel="stylesheet">
<style>
:root{
  --blue:#2f5ff0;
  --hero:#3f6af1;
  --navy:#1c2740;
  --navy-2:#2a3654;
  --ink:#1b2233;
  --muted:#8b93a5;
  --line:#e6e9f0;
  --green:#22c55e;
  --red:#ef3b3b;
  --yellow:#fbbf24;
  --page:#ffffff;
  --panel:#f4f6fa;
}
*{box-sizing:border-box;margin:0;padding:0}
html,body{width:1200px;height:2880px;overflow:hidden;background:var(--page)}
body{position:relative;font-family:"Poppins",sans-serif;color:var(--ink)}
.hero{position:absolute;left:0;top:0;width:1200px;height:938px;background:var(--hero);overflow:hidden}
.hero-copy{position:absolute;left:45px;top:160px;color:#fff}
.eyebrow{display:flex;align-items:center;gap:10px;font-family:"Montserrat",sans-serif;font-weight:800;font-size:29px;letter-spacing:2px}
.eyebrow .mark{width:24px;height:24px;border:2px solid #fff;border-radius:4px}
.hero-title{font-family:"Montserrat",sans-serif;font-weight:800;font-size:45px;margin-top:20px;letter-spacing:.5px}
.hero-sub{font-weight:300;font-size:31px;margin-top:8px}
.features{list-style:none;margin-top:56px}
.features li{display:flex;align-items:center;gap:12px;font-size:24px;font-weight:400;height:37.5px}
.features li::before{content:"";width:13px;height:13px;background:#fff;transform:rotate(45deg);border-radius:2px}

.panel{position:absolute;background:var(--panel);border-radius:4px}

.phone{position:absolute;width:270px;height:578px;background:#fff;border-radius:22px;box-shadow:0 14px 40px rgba(30,50,110,.14);overflow:hidden}
.hero .phone{box-shadow:0 20px 50px rgba(10,30,110,.25);transform:rotate(-35deg) scale(1.12)}
.chat-head{position:absolute;left:0;top:0;width:100%;height:62px;border-bottom:1px solid var(--line)}
.chat-head .close{position:absolute;left:30px;top:26px;width:12px;height:12px}
.chat-head .name{position:absolute;left:0;right:0;top:24px;text-align:center;font-size:12.5px;font-weight:500}
.chat-head .info{position:absolute;right:28px;top:23px;width:19px;height:19px;border-radius:50%;background:var(--blue);color:#fff;font-size:11px;font-weight:700;text-align:center;line-height:19px}
.avatar{position:absolute;border-radius:50%;width:64px;height:64px}
.avatar.caller{left:52px;top:82px;background:radial-gradient(circle at 45% 40%,#e08a55,#8a3b2a 60%,#3d6fa8)}
.avatar.contact{left:154px;top:80px;background:radial-gradient(circle at 50% 45%,#b8876a,#5b4236 60%,#8fa0a8)}
.avatar.ring{box-shadow:0 0 0 3px #fff,0 0 0 5px var(--blue)}
.link-dots{position:absolute;left:122px;top:109px;display:flex;gap:3px}
.link-dots i{width:4px;height:4px;border-radius:50%;background:#9aa1b0}
.link-dots.live i{background:var(--blue)}
.transcript{position:absolute;left:49px;top:164px;width:171px;height:47px;border:1.5px solid var(--blue);border-radius:6px;text-align:center;line-height:44px;font-size:11px;color:var(--blue);white-space:nowrap}
.transcript .tag{position:absolute;left:50%;top:-8px;transform:translateX(-50%);background:var(--blue);color:#fff;font-size:6.5px;line-height:13px;padding:0 10px;border-radius:3px;white-space:nowrap}
.transcript.idle{color:var(--muted)}
.emo{position:absolute;top:200px;display:flex;gap:3px}
.emo i{width:13px;height:13px;border-radius:50%;border:2px solid #fff}
.emo .b{background:#5b8cf6}.emo .r{background:var(--red)}.emo .y{background:var(--yellow)}

.msg{position:absolute;font-size:6.5px;color:var(--ink)}
.msg .row{display:flex;align-items:center;gap:8px}
.msg svg.wave{width:80px;height:18px;color:#7d8597}
.msg .btn{width:18px;height:18px;border-radius:50%;background:var(--blue);display:grid;place-items:center}
.msg .cap{display:flex;gap:16px;margin-top:3px;white-space:nowrap}
.msg.in{left:35px}
.msg.in.playing svg.wave{color:#5b8cf6}
.msg.in.playing .cap{color:#5b8cf6}
.msg.out{left:125px;top:293px;width:127px;height:40px;background:var(--blue);border-radius:4px;padding:5px 10px;color:#fff}
.msg.out svg.wave{color:#fff;width:78px}
.msg.out .btn{background:#fff}
.stamp{position:absolute;font-size:7px;color:var(--muted);white-space:nowrap}
.typing{position:absolute;left:209px;top:426px;width:43px;height:17px;border-radius:5px;background:var(--blue);display:flex;gap:3px;align-items:center;justify-content:center}
.typing i{width:3px;height:3px;border-radius:50%;background:#fff}

.action-bar{position:absolute;left:18px;top:508px;width:234px;height:47px;background:var(--navy);border-radius:6px}
.action-bar .act{position:absolute;top:9px;height:29px;border-radius:4px;background:var(--navy-2);display:flex;align-items:center;gap:5px;padding:0 11px;font-size:9px;color:#6f7a93}
.action-bar .cancel{left:8px}
.action-bar .send{right:8px}
.is-recording .action-bar .cancel{color:var(--red)}
.is-recording .action-bar .send{color:var(--green)}
.pulse{position:absolute;left:69px;top:440px;width:132px;height:132px;border-radius:50%;background:radial-gradient(circle,rgba(47,95,240,.14) 0 45%,rgba(47,95,240,.07) 46% 100%)}
.mic{position:absolute;left:106px;top:478px;width:58px;height:58px;border-radius:50%;background:var(--blue);display:grid;place-items:center;box-shadow:0 6px 16px rgba(47,95,240,.35);color:#fff}
.mic .timer{font-size:7px;text-align:center;line-height:1.3}

.status{position:absolute;left:27px;top:18px;font-size:10px;font-weight:600}
.status-icons{position:absolute;right:20px;top:20px;display:flex;gap:3px;align-items:center}
.home-title{position:absolute;left:0;right:0;top:48px;text-align:center;font-size:15px;font-weight:400}
.sec{position:absolute;left:21px;font-size:11px;font-weight:500}
.viewall{position:absolute;right:20px;font-size:8px;color:var(--muted)}
.profile-card{position:absolute;left:19px;top:112px;width:236px;height:62px;border-radius:6px;box-shadow:0 2px 10px rgba(20,30,60,.08)}
.profile-card .pic{position:absolute;left:10px;top:8px;width:46px;height:46px;border-radius:4px;background:linear-gradient(135deg,#b8876a,#4e3a30)}
.profile-card .who{position:absolute;left:68px;top:8px;font-size:10px;font-weight:500;white-space:nowrap}
.profile-card .age{position:absolute;left:68px;top:23px;font-size:7px;color:var(--muted)}
.profile-card .badge{position:absolute;left:68px;top:38px;background:var(--green);color:#fff;font-size:7px;padding:2px 10px;border-radius:2px}
.profile-card .edit{position:absolute;right:10px;top:12px;width:18px;height:18px;border-radius:50%;background:#eef1f6;display:grid;place-items:center}
.contact{position:absolute;top:216px;width:70px;height:77px;border-radius:6px;box-shadow:0 2px 10px rgba(20,30,60,.08);text-align:center;font-size:8px;color:var(--muted);line-height:1.2}
.contact.add{border:1.5px dashed #c7ccd8;box-shadow:none}
.contact .thumb{width:34px;height:34px;border-radius:50%;margin:10px auto 7px}
.contact .plus{width:20px;height:20px;border:1.5px solid var(--blue);border-radius:50%;margin:16px auto 10px;color:var(--blue);font-size:14px;line-height:16px}
.last{position:absolute;left:19px;width:236px;height:46px;border-radius:6px;box-shadow:0 2px 10px rgba(20,30,60,.08)}
.last .thumb{position:absolute;left:10px;top:8px;width:30px;height:30px;border-radius:4px}
.last .who{position:absolute;left:52px;top:9px;font-size:9px;font-weight:500;white-space:nowrap}
.last .txt{position:absolute;left:52px;top:24px;font-size:6.5px;color:var(--muted);white-space:nowrap}
.last .time{position:absolute;right:12px;top:9px;font-size:6.5px;color:var(--muted)}
.last .count{position:absolute;right:14px;top:25px;width:12px;height:12px;border-radius:50%;background:var(--red);color:#fff;font-size:7px;text-align:center;line-height:12px}
.tabbar{position:absolute;left:19px;top:522px;width:236px;height:48px;background:var(--navy);border-radius:6px;display:flex;align-items:center;justify-content:space-around;padding:0 6px}
.tab{display:flex;align-items:center;gap:4px;font-size:9px;font-weight:600;color:#fff;padding:7px 10px;border-radius:4px;white-space:nowrap}
.tab.active{background:var(--blue)}

.heading{position:absolute;font-family:"Montserrat",sans-serif;font-weight:800;font-size:35px;line-height:44px;letter-spacing:1px;color:var(--ink)}
.heading.wide{font-size:36px;line-height:45px}
.note{position:absolute;font-size:23px;color:var(--ink);white-space:nowrap}
.note.strong{font-size:19px;font-weight:600;line-height:29px}
.note.small{font-size:15.5px;line-height:26px}
.leader{position:absolute;height:2px;background:var(--ink)}
</style>
</head>
<body>
<svg width="0" height="0" style="position:absolute">
  <defs>
    <symbol id="wave" viewBox="0 0 80 18">
      <path d="M1 7v4M4 5v8M7 8v2M10 3v12M13 6v6M16 8v2M19 2v14M22 5v8M25 7v4M28 4v10M31 6v6M34 8v2M37 3v12M40 6v6M43 1v16M46 5v8M49 7v4M52 4v10M55 6v6M58 8v2M61 3v12M64 5v8M67 7v4M70 4v10M73 6v6M76 8v2M79 7v4" stroke="currentColor" stroke-width="1.2" fill="none"/>
    </symbol>
    <symbol id="play" viewBox="0 0 10 10"><path d="M3 2l5 3-5 3z" fill="currentColor"/></symbol>
    <symbol id="pause" viewBox="0 0 10 10"><path d="M3 2h1.5v6H3zM5.5 2H7v6H5.5z" fill="currentColor"/></symbol>
    <symbol id="micro" viewBox="0 0 20 20"><rect x="7" y="2" width="6" height="10" rx="3" fill="currentColor"/><path d="M4.5 9a5.5 5.5 0 0 0 11 0M10 14.5V18M7 18h6" stroke="currentColor" stroke-width="1.6" fill="none" stroke-linecap="round"/></symbol>
    <symbol id="xcircle" viewBox="0 0 12 12"><circle cx="6" cy="6" r="5" stroke="currentColor" fill="none"/><path d="M4 4l4 4M8 4l-4 4" stroke="currentColor"/></symbol>
    <symbol id="sendic" viewBox="0 0 12 12"><path d="M1 1l10 5-10 5 2-5z" stroke="currentColor" fill="none" stroke-linejoin="round"/></symbol>
    <symbol id="cross" viewBox="0 0 12 12"><path d="M1 1l10 10M11 1L1 11" stroke="#1b2233" stroke-width="1.6"/></symbol>
  </defs>
</svg>

<section class="hero">
  <div class="hero-copy">
    <div class="eyebrow"><span class="mark"></span>UI DESIGN</div>
    <h1 class="hero-title">HOMEPAGE</h1>
    <p class="hero-sub">Voice Message App</p>
    <ul class="features">
      <li>Voice to Transcript</li>
      <li>Record</li>
      <li>Listen to New Message</li>
      <li>Reply with Emoticon</li>
      <li>Modern yet user friendly design</li>
    </ul>
  </div>

  <div class="phone" style="left:690px;top:-130px">
    <div class="chat-head"><svg class="close"><use href="#cross"/></svg><div class="name">Liam Porter</div><div class="info">i</div></div>
    <div class="avatar caller ring" role="img" aria-label="Caller portrait photo"></div>
    <div class="link-dots live"><i></i><i></i><i></i></div>
    <div class="avatar contact" role="img" aria-label="Contact portrait photo"></div>
    <div class="transcript"><span class="tag">Transcript 0:09</span>Thank you! That wa...</div>
    <div class="emo" style="left:185px"><i class="b"></i><i class="r"></i><i class="y"></i></div>
    <div class="msg in playing" style="top:232px"><div class="row"><svg class="wave"><use href="#wave"/></svg><span class="btn" style="color:#fff"><svg width="10" height="10"><use href="#pause"/></svg></span></div><div class="cap"><span>Thank you! That wa...</span><span>0:09</span></div></div>
    <div class="stamp" style="left:35px;top:274px">09:10 AM</div>
    <div class="msg out"><div class="row"><span class="btn" style="color:var(--blue)"><svg width="10" height="10"><use href="#play"/></svg></span><svg class="wave"><use href="#wave"/></svg></div><div class="cap"><span>0:02</span><span>We are going now</span></div></div>
    <div class="stamp" style="right:18px;top:339px">09:16 AM ✓</div>
    <div class="msg in" style="top:356px"><div class="row"><svg class="wave"><use href="#wave"/></svg><span class="btn" style="color:#fff"><svg width="10" height="10"><use href="#play"/></svg></span></div><div class="cap"><span>I'm on meeting, can you pleas...</span><span>0:16</span></div></div>
    <div class="stamp" style="left:35px;top:398px">09:25 AM</div>
    <div class="action-bar"><span class="act cancel"><svg width="10" height="10"><use href="#xcircle"/></svg>Cancel</span><span class="act send"><svg width="10" height="10"><use href="#sendic"/></svg>Send</span></div>
    <div class="mic"><svg width="20" height="20"><use href="#micro"/></svg></div>
  </div>

  <div class="phone" style="left:580px;top:322px">
    <div class="status">9:41</div>
    <div class="status-icons"><svg width="30" height="9"><rect x="0" y="5" width="2" height="4" fill="#1b2233"/><rect x="3" y="3" width="2" height="6" fill="#1b2233"/><rect x="6" y="1" width="2" height="8" fill="#1b2233"/><rect x="15" y="1" width="14" height="7" rx="2" fill="#1b2233"/></svg></div>
    <div class="home-title">Home</div>
    <div class="sec" style="top:92px">Your Profile</div>
    <div class="profile-card"><div class="pic" role="img" aria-label="Profile photo"></div><div class="who">Marco Delvantis</div><div class="age">63 years old</div><div class="badge">Verified User</div></div>
    <div class="sec" style="top:193px">Contact List</div><div class="viewall" style="top:195px">View All</div>
    <div class="contact add" style="left:21px"><div class="plus">+</div>Add New<br>Contact</div>
    <div class="contact" style="left:101px"><div class="thumb" style="background:#d9c9a8" role="img" aria-label="Contact photo"></div>Rina<br>Solvara</div>
    <div class="contact" style="left:181px"><div class="thumb" style="background:#6d6257" role="img" aria-label="Contact photo"></div>Nadia<br>Gunter</div>
    <div class="sec" style="top:318px">Last Message</div><div class="viewall" style="top:320px">View All</div>
    <div class="last" style="top:344px"><div class="thumb" style="background:#c96a45" role="img" aria-label="Contact photo"></div><div class="who">Liam Porter</div><div class="txt">Thank you! That was amazing jan...</div><div class="time">09:16 PM</div><div class="count">1</div></div>
    <div class="last" style="top:400px"><div class="thumb" style="background:#3e3a36" role="img" aria-label="Contact photo"></div><div class="who">Adam Kareem</div><div class="txt">✓ Thank you! That was amazing jan...</div><div class="time">05:36 PM</div></div>
    <div class="last" style="top:456px"><div class="thumb" style="background:#5fb2b0" role="img" aria-label="Contact photo"></div><div class="who">Fiona Hartwell</div><div class="txt">✓ On my way right now</div><div class="time">10:36 AM</div></div>
    <div class="tabbar"><span class="tab active">⌂ Home</span><span class="tab">◯ Message</span><span class="tab">⚙ Setting</span></div>
  </div>

  <div class="phone" style="left:335px;top:600px">
    <div class="chat-head"><svg class="close"><use href="#cross"/></svg><div class="name">Liam Porter</div><div class="info">i</div></div>
    <div class="avatar caller" role="img" aria-label="Caller portrait photo"></div>
    <div class="link-dots live"><i></i><i></i><i></i></div>
    <div class="avatar contact ring" role="img" aria-label="Contact portrait photo"></div>
    <div class="transcript"><span class="tag">Transcript 0:33</span>... Sure will do it now ...</div>
  </div>

  <div class="phone" style="left:960px;top:410px">
    <div class="chat-head"><svg class="close"><use href="#cross"/></svg><div class="name">Liam Porter</div><div class="info">i</div></div>
    <div class="avatar caller ring" role="img" aria-label="Caller portrait photo"></div>
    <div class="link-dots live"><i></i><i></i><i></i></div>
    <div class="avatar contact" role="img" aria-label="Contact portrait photo"></div>
    <div class="transcript"><span class="tag">Transcript 0:09</span>Thank you! That wa...</div>
    <div class="emo" style="left:214px"><i class="y"></i></div>
    <div class="msg in playing" style="top:232px"><div class="row"><svg class="wave"><use href="#wave"/></svg><span class="btn" style="color:#fff"><svg width="10" height="10"><use href="#pause"/></svg></span></div><div class="cap"><span>Thank you! That wa...</span><span>0:09</span></div></div>
    <div class="stamp" style="left:35px;top:274px">09:10 AM</div>
  </div>
</section>

<div class="panel" style="left:40px;top:960px;width:870px;height:615px"></div>

<div class="phone" style="left:61px;top:970px">
  <div class="chat-head"><svg class="close"><use href="#cross"/></svg><div class="name">Liam Porter</div><div class="info">i</div></div>
  <div class="avatar caller" role="img" aria-label="Caller portrait photo"></div>
  <div class="link-dots"><i></i><i></i><i></i><i></i></div>
  <div class="avatar contact" role="img" aria-label="Contact portrait photo"></div>
  <div class="transcript idle"><span class="tag">Transcript</span>...</div>
  <div class="msg in" style="top:232px"><div class="row"><svg class="wave"><use href="#wave"/></svg><span class="btn" style="color:#fff"><svg width="10" height="10"><use href="#play"/></svg></span></div><div class="cap"><span>Thank you! That wa...</span><span>0:09</span></div></div>
  <div class="stamp" style="left:35px;top:274px">09:10 AM</div>
  <div class="msg out"><div class="row"><span class="btn" style="color:var(--blue)"><svg width="10" height="10"><use href="#play"/></svg></span><svg class="wave"><use href="#wave"/></svg></div><div class="cap"><span>0:02</span><span>We are going now</span></div></div>
  <div class="stamp" style="right:18px;top:339px">09:16 AM ✓</div>
  <div class="msg in" style="top:356px"><div class="row"><svg class="wave"><use href="#wave"/></svg><span class="btn" style="color:#fff"><svg width="10" height="10"><use href="#play"/></svg></span></div><div class="cap"><span>I'm on meeting, can you pleas...</span><span>0:16</span></div></div>
  <div class="stamp" style="left:35px;top:398px">09:25 AM</div>
  <div class="action-bar"><span class="act cancel"><svg width="10" height="10"><use href="#xcircle"/></svg>Cancel</span><span class="act send"><svg width="10" height="10"><use href="#sendic"/></svg>Send</span></div>
  <div class="mic"><svg width="20" height="20"><use href="#micro"/></svg></div>
</div>

<h2 class="heading" style="left:369px;top:978px">Idle<br>Screen</h2>
<div class="leader" style="left:295px;top:1160px;width:62px"></div>
<div class="note" style="left:369px;top:1143px">Transcript Box</div>
<div class="leader" style="left:321px;top:1502px;width:32px"></div>
<div class="note strong" style="left:370px;top:1478px">Disable<br>Action Button</div>

<div class="phone is-recording" style="left:596px;top:970px">
  <div class="chat-head"><svg class="close"><use href="#cross"/></svg><div class="name">Liam Porter</div><div class="info">i</div></div>
  <div class="avatar caller" role="img" aria-label="Caller portrait photo"></div>
  <div class="link-dots live"><i></i><i></i><i></i></div>
  <div class="avatar contact ring" role="img" aria-label="Contact portrait photo"></div>
  <div class="transcript"><span class="tag">Transcript 0:33</span>... Sure will do it now ...</div>
  <div class="msg in" style="top:232px"><div class="row"><svg class="wave"><use href="#wave"/></svg><span class="btn" style="color:#fff"><svg width="10" height="10"><use href="#play"/></svg></span></div><div class="cap"><span>Thank you! That wa...</span><span>0:09</span></div></div>
  <div class="stamp" style="left:35px;top:274px">09:10 AM</div>
  <div class="msg out"><div class="row"><span class="btn" style="color:var(--blue)"><svg width="10" height="10"><use href="#play"/></svg></span><svg class="wave"><use href="#wave"/></svg></div><div class="cap"><span>0:02</span><span>We are going now</span></div></div>
  <div class="stamp" style="right:18px;top:339px">09:16 AM ✓</div>
  <div class="msg in" style="top:356px"><div class="row"><svg class="wave"><use href="#wave"/></svg><span class="btn" style="color:#fff"><svg width="10" height="10"><use href="#play"/></svg></span></div><div class="cap"><span>I'm on meeting, can you pleas...</span><span>0:16</span></div></div>
  <div class="stamp" style="left:35px;top:398px">09:25 AM</div>
  <div class="typing"><i></i><i></i><i></i></div>
  <div class="pulse"></div>
  <div class="action-bar"><span class="act cancel"><svg width="10" height="10"><use href="#xcircle"/></svg>Cancel</span><span class="act send"><svg width="10" height="10"><use href="#sendic"/></svg>Send</span></div>
  <div class="mic"><div class="timer">00:33<br>●●●</div></div>
</div>

<h2 class="heading" style="left:903px;top:978px">Reply<br>Screen</h2>
<div class="note strong" style="left:909px;top:1407px">Active Action Button</div>
<div class="note small" style="left:909px;top:1438px">Delete Last Sentence<br>Send Message<br>Hold <i>Record Button</i> to keep<br>the recording going</div>
<div class="leader" style="left:875px;top:1502px;width:18px"></div>

<div class="panel" style="left:40px;top:1598px;width:900px;height:630px"></div>

<div class="phone" style="left:64px;top:1607px">
  <div class="chat-head"><svg class="close"><use href="#cross"/></svg><div class="name">Liam Porter</div><div class="info">i</div></div>
  <div class="avatar caller ring" role="img" aria-label="Caller portrait photo"></div>
  <div class="link-dots live"><i></i><i></i><i></i></div>
  <div class="avatar contact" role="img" aria-label="Contact portrait photo"></div>
  <div class="transcript"><span class="tag">Transcript 0:09</span>Thank you! That wa...</div>
  <div class="emo" style="left:214px"><i class="y"></i></div>
  <div class="msg in playing" style="top:232px"><div class="row"><svg class="wave"><use href="#wave"/></svg><span class="btn" style="color:#fff"><svg width="10" height="10"><use href="#pause"/></svg></span></div><div class="cap"><span>Thank you! That wa...</span><span>0:09</span></div></div>
  <div class="stamp" style="left:35px;top:274px">09:10 AM</div>
  <div class="msg out"><div class="row"><span class="btn" style="color:var(--blue)"><svg width="10" height="10"><use href="#play"/></svg></span><svg class="wave"><use href="#wave"/></svg></div><div class="cap"><span>0:02</span><span>We are going now</span></div></div>
  <div class="stamp" style="right:18px;top:339px">09:16 AM ✓</div>
  <div class="msg in" style="top:356px"><div class="row"><svg class="wave"><use href="#wave"/></svg><span class="btn" style="color:#fff"><svg width="10" height="10"><use href="#play"/></svg></span></div><div class="cap"><span>I'm on meeting, can you pleas...</span><span>0:16</span></div></div>
  <div class="stamp" style="left:35px;top:398px">09:25 AM</div>
  <div class="action-bar"><span class="act cancel"><svg width="10" height="10"><use href="#xcircle"/></svg>Cancel</span><span class="act send"><svg width="10" height="10"><use href="#sendic"/></svg>Send</span></div>
  <div class="mic"><svg width="20" height="20"><use href="#micro"/></svg></div>
</div>

<h2 class="heading" style="left:378px;top:1616px">Listen<br>Message</h2>
<div class="leader" style="left:302px;top:1826px;width:65px"></div>
<div class="note" style="left:377px;top:1810px">Form of Emoticons</div>

<div class="phone" style="left:609px;top:1607px">
  <div class="chat-head"><svg class="close"><use href="#cross"/></svg><div class="name">Liam Porter</div><div class="info">i</div></div>
  <div class="avatar caller ring" role="img" aria-label="Caller portrait photo"></div>
  <div class="link-dots live"><i></i><i></i><i></i></div>
  <div class="avatar contact" role="img" aria-label="Contact portrait photo"></div>
  <div class="transcript"><span class="tag">Transcript 0:09</span>Thank you! That wa...</div>
  <div class="emo" style="left:174px"><i class="b"></i><i class="r"></i><i class="y"></i></div>
  <div class="msg in playing" style="top:232px"><div class="row"><svg class="wave"><use href="#wave"/></svg><span class="btn" style="color:#fff"><svg width="10" height="10"><use href="#pause"/></svg></span></div><div class="cap"><span>Thank you! That wa...</span><span>0:09</span></div></div>
  <div class="stamp" style="left:35px;top:274px">09:10 AM</div>
  <div class="msg out"><div class="row"><span class="btn" style="color:var(--blue)"><svg width="10" height="10"><use href="#play"/></svg></span><svg class="wave"><use href="#wave"/></svg></div><div class="cap"><span>0:02</span><span>We are going now</span></div></div>
  <div class="stamp" style="right:18px;top:339px">09:16 AM ✓</div>
  <div class="msg in" style="top:356px"><div class="row"><svg class="wave"><use href="#wave"/></svg><span class="btn" style="color:#fff"><svg width="10" height="10"><use href="#play"/></svg></span></div><div class="cap"><span>I'm on meeting, can you pleas...</span><span>0:16</span></div></div>
  <div class="stamp" style="left:35px;top:398px">09:25 AM</div>
  <div class="action-bar"><span class="act cancel"><svg width="10" height="10"><use href="#xcircle"/></svg>Cancel</span><span class="act send"><svg width="10" height="10"><use href="#sendic"/></svg>Send</span></div>
  <div class="mic"><svg width="20" height="20"><use href="#micro"/></svg></div>
</div>

<div class="leader" style="left:846px;top:1826px;width:65px"></div>
<div class="note" style="left:921px;top:1810px">Choose Emoticons</div>

<div class="panel" style="left:40px;top:2248px;width:310px;height:620px"></div>

<div class="phone" style="left:64px;top:2260px;height:587px">
  <div class="status">9:41</div>
  <div class="status-icons"><svg width="30" height="9"><rect x="0" y="5" width="2" height="4" fill="#1b2233"/><rect x="3" y="3" width="2" height="6" fill="#1b2233"/><rect x="6" y="1" width="2" height="8" fill="#1b2233"/><rect x="15" y="1" width="14" height="7" rx="2" fill="#1b2233"/></svg></div>
  <div class="home-title">Home</div>
  <div class="sec" style="top:92px">Your Profile</div>
  <div class="profile-card"><div class="pic" role="img" aria-label="Profile photo"></div><div class="who">Marco Delvantis</div><div class="age">63 years old</div><div class="badge">Verified User</div><div class="edit"><svg width="9" height="9" viewBox="0 0 10 10"><circle cx="5" cy="3" r="2.2" fill="#1b2233"/><path d="M1 10a4 4 0 0 1 8 0z" fill="#1b2233"/></svg></div></div>
  <div class="sec" style="top:193px">Contact List</div><div class="viewall" style="top:195px">View All</div>
  <div class="contact add" style="left:21px"><div class="plus">+</div>Add New<br>Contact</div>
  <div class="contact" style="left:101px"><div class="thumb" style="background:#d9c9a8" role="img" aria-label="Contact photo"></div>Rina<br>Solvara</div>
  <div class="contact" style="left:181px"><div class="thumb" style="background:#6d6257" role="img" aria-label="Contact photo"></div>Nadia<br>Gunter</div>
  <div class="sec" style="top:318px">Last Message</div><div class="viewall" style="top:320px">View All</div>
  <div class="last" style="top:344px"><div class="thumb" style="background:#c96a45" role="img" aria-label="Contact photo"></div><div class="who">Liam Porter</div><div class="txt">Thank you! That was amazing jan...</div><div class="time">09:16 PM</div><div class="count">1</div></div>
  <div class="last" style="top:400px"><div class="thumb" style="background:#3e3a36" role="img" aria-label="Contact photo"></div><div class="who">Adam Kareem</div><div class="txt">✓ Thank you! That was amazing jan...</div><div class="time">05:36 PM</div></div>
  <div class="last" style="top:456px"><div class="thumb" style="background:#5fb2b0" role="img" aria-label="Contact photo"></div><div class="who">Fiona Hartwell</div><div class="txt">✓ On my way right now</div><div class="time">10:36 AM</div></div>
  <div class="tabbar"><span class="tab active">⌂ Home</span><span class="tab">◯ Message</span><span class="tab">⚙ Setting</span></div>
</div>

<h2 class="heading wide" style="left:378px;top:2268px">Additional Homepage<br>UI Design Exploration</h2>
<div class="leader" style="left:335px;top:2401px;width:64px"></div>
<div class="note" style="left:409px;top:2384px">User profile card</div>
<div class="leader" style="left:335px;top:2456px;width:64px"></div>
<div class="note" style="left:409px;top:2439px">User added contact</div>
<div class="leader" style="left:335px;top:2586px;width:64px"></div>
<div class="note" style="left:409px;top:2569px">Last message received</div>
<div class="leader" style="left:335px;top:2805px;width:64px"></div>
<div class="note" style="left:409px;top:2788px">Bottom Navigation Bar</div>
</body>
</html>
```